Custom Label for Women's Supplement Brand

Need a product label for our products, we have a logo designed but need to incorporate it in to our product line which will have capsule bottles, tincture bottles, and eventually skin care. We originally wanted a label that had black as main color, but are open to options. Want it to be sleek, and pull the eye, simple yet fun. Even something different that doesn’t look like anyone else.
Updates

Low designer entries

Target Market(s)

Women 26-70

Requirements
Nice to have
• Would love some metallic accents

```html
<!DOCTYPE html>
<html lang="en">
<head>
<meta charset="utf-8">
<title>Skin Care Labels</title>
<link href="https://fonts.googleapis.com/css2?family=Bebas+Neue&family=Montserrat:wght@400;500;600;700;800&display=swap" rel="stylesheet">
<style>
  :root{
    --ink:#0c0c0c;
    --ink-soft:#1c1c1c;
    --lime:#dcf725;
    --lime-deep:#a9c93a;
    --cyan:#2fd6dc;
    --cyan-deep:#1aa5b8;
    --brand-green:#8fae3c;
    --white:#ffffff;
    --metal-dark:#3a3a3a;
    --metal-light:#bdbdbd;
    --nutri-red:#e2553f;
    --nutri-cream:#f8eedb;
    --nutri-ink:#3b2f28;
    --page:#ffffff;
  }
  *{margin:0;padding:0;box-sizing:border-box;}
  html,body{width:710px;height:1200px;overflow:hidden;background:var(--page);}
  body{position:relative;font-family:"Montserrat",sans-serif;}

  .label-frame{position:absolute;overflow:hidden;}
  .label-frame--capsules{left:25px;top:290px;width:660px;height:316px;}
  .label-frame--drops{left:69px;top:652px;width:572px;height:274px;}

  .label{position:absolute;left:0;top:0;width:1160px;height:556px;transform-origin:0 0;color:var(--white);}
  .label-frame--capsules .label{transform:scale(0.569);}
  .label-frame--drops .label{transform:scale(0.493);}

  .label__base{position:absolute;inset:0;}
  .label__texture{position:absolute;left:0;top:8px;width:1160px;height:486px;
    background:radial-gradient(ellipse at 45% 40%, #262626 0%, #121212 55%, #070707 100%);
    clip-path:polygon(0 0,100% 0,100% 486px,560px 486px,532px 456px,0 456px);}

  .info-block{position:absolute;left:36px;width:272px;}
  .info-block__title{font-weight:700;font-size:17px;color:var(--lime);letter-spacing:.2px;margin-bottom:10px;}
  .info-block__text{font-size:12px;line-height:15px;font-weight:500;}
  .info-block--ingredients{top:50px;}
  .info-block--usage{top:199px;}

  .brand{position:absolute;left:420px;width:310px;top:104px;text-align:center;
    font-weight:600;font-size:25px;color:var(--brand-green);letter-spacing:.3px;}

  .product-title{position:absolute;left:420px;width:310px;top:166px;text-align:center;font-family:"Bebas Neue",sans-serif;line-height:1;}
  .product-title__line{display:block;font-size:84px;letter-spacing:-.5px;}
  .product-title__line--top{color:var(--white);}
  .product-title__line--bottom{color:var(--cyan);margin-top:-14px;}

  .count-badge{position:absolute;left:440px;top:342px;width:90px;height:90px;border:3px solid var(--cyan);border-radius:50%;
    display:flex;flex-direction:column;align-items:center;justify-content:center;}
  .count-badge__number{font-weight:800;font-size:38px;line-height:34px;}
  .count-badge__unit{font-weight:700;font-size:10.5px;}

  .benefits{position:absolute;left:543px;top:360px;font-size:12.5px;line-height:15.5px;font-weight:500;text-transform:uppercase;}

  .dose{position:absolute;left:422px;top:472px;display:flex;align-items:center;color:var(--ink);z-index:2;}
  .dose__number{font-size:44px;font-weight:500;line-height:1;margin-right:4px;}
  .dose__text{font-size:15px;line-height:17px;text-transform:uppercase;font-weight:500;}
  .formula-note{position:absolute;left:538px;top:499px;font-size:11.5px;font-weight:500;color:var(--white);text-transform:uppercase;z-index:2;}

  .benefit-icons{position:absolute;left:795px;top:72px;width:80px;}
  .benefit-icon{position:absolute;left:0;width:80px;text-align:center;}
  .benefit-icon__ring{width:66px;height:66px;margin:0 auto;border:3px solid var(--cyan);border-radius:50%;
    background:radial-gradient(circle, #2a2f30 0%, #141414 75%);}
  .benefit-icon__label{font-size:9.5px;font-weight:500;line-height:11px;margin-top:3px;}
  .benefit-icon:nth-child(1){top:0;}
  .benefit-icon:nth-child(2){top:98px;}
  .benefit-icon:nth-child(3){top:198px;}
  .benefit-icon:nth-child(4){top:300px;}

  .nutrition{position:absolute;left:900px;top:80px;width:178px;height:225px;background:var(--nutri-cream);border-radius:6px;overflow:hidden;color:var(--nutri-ink);}
  .nutrition__header{background:var(--nutri-red);color:var(--white);font-size:11.5px;font-weight:500;text-align:center;height:28px;line-height:30px;}
  .nutrition__serving{font-size:5px;text-align:center;margin-top:7px;border-bottom:.5px solid #b8a991;margin-left:12px;margin-right:12px;padding-bottom:2px;}
  .nutrition__summary{display:flex;justify-content:space-between;align-items:center;margin:3px 12px 0;font-size:5px;border-bottom:.5px solid #b8a991;padding-bottom:4px;}
  .nutrition__summary strong{font-size:9.5px;font-weight:600;}
  .nutrition__amount{font-size:5px;font-weight:600;margin:6px 12px 4px;}
  .nutrition__table{margin:0 18px;border-collapse:collapse;width:142px;font-size:5px;border:.5px solid #b8a991;}
  .nutrition__table td{padding:2.3px 3px;border-bottom:.5px solid #cdbfa8;}
  .nutrition__table td:nth-child(2){width:40px;}
  .nutrition__table td:nth-child(3){text-align:right;width:24px;}
  .nutrition__note{font-size:4.4px;line-height:5px;margin:4px 18px 0;}

  .warning{position:absolute;left:900px;top:322px;width:200px;}
  .warning__title{font-size:17px;font-weight:700;color:var(--lime);}
  .warning__text{font-size:9.6px;line-height:11.8px;font-weight:500;margin-top:3px;}
  .shelf-life{position:absolute;left:900px;top:398px;font-size:11.4px;line-height:14px;font-weight:500;text-transform:uppercase;}
  .shelf-life__title{color:var(--lime);}
</style>
</head>
<body>

<section class="label-frame label-frame--capsules">
  <article class="label">
    <svg class="label__base" width="1160" height="556" viewBox="0 0 1160 556">
      <defs>
        <linearGradient id="limeBand" x1="0" y1="0" x2="1" y2="0">
          <stop offset="0" stop-color="#c4e033"/>
          <stop offset="0.5" stop-color="#e2fb22"/>
          <stop offset="1" stop-color="#a9c93a"/>
        </linearGradient>
        <linearGradient id="metalBand" x1="0" y1="0" x2="1" y2="0">
          <stop offset="0" stop-color="#3a3a3a"/>
          <stop offset="0.6" stop-color="#8a8a8a"/>
          <stop offset="1" stop-color="#c8c8c8"/>
        </linearGradient>
      </defs>
      <rect x="0" y="0" width="1160" height="556" fill="url(#limeBand)"/>
      <polygon points="0,0 1160,0 1160,494 560,494 532,464 0,464" fill="#0c0c0c"/>
    </svg>
    <div class="label__texture" role="img" aria-label="Dark geometric chevron pattern background"></div>
    <svg class="label__base" width="1160" height="556" viewBox="0 0 1160 556" aria-hidden="true">
      <polyline points="0,462 530,462 558,490 1160,490" fill="none" stroke="#555" stroke-width="4"/>
      <polygon points="0,0 1160,0 1160,32 690,32 660,6 0,6" fill="url(#metalBand)"/>
    </svg>

    <div class="info-block info-block--ingredients">
      <h3 class="info-block__title">INGRIDIENTS</h3>
      <p class="info-block__text">Lorem ipsum dolor sit amet, consectetur adipiscing elit, sed do eiusmod tempor incididunt ut labore et dolore magna aliqua. Quis ipsum suspendisse ultrices gravida. Risus commodo viverra maecenas accumsan lacus vel facilisis.</p>
    </div>
    <div class="info-block info-block--usage">
      <h3 class="info-block__title">HOW TO USE</h3>
      <p class="info-block__text">Lorem ipsum dolor sit amet, consectetur adipiscing elit, sed do eiusmod tempor incididunt ut labore et dolore magna aliqua. Quis ipsum suspendisse ultrices gravida. Risus commodo viverra maecenas accumsan lacus vel facilisis.</p>
    </div>

    <div class="brand">Calm Bloom Wellness</div>
    <h1 class="product-title">
      <span class="product-title__line product-title__line--top">SKIN CARE</span>
      <span class="product-title__line product-title__line--bottom">CAPSULES</span>
    </h1>
    <div class="count-badge"><span class="count-badge__number">30</span><span class="count-badge__unit">CAPSULES</span></div>
    <p class="benefits">Beauty &amp; Wellness<br>Improves Comlextions<br>Anti Aging</p>

    <div class="dose"><span class="dose__number">1</span><span class="dose__text">Capsule<br>Per Day</span></div>
    <p class="formula-note">Advanced Skin Care Formula</p>

    <div class="benefit-icons">
      <div class="benefit-icon"><div class="benefit-icon__ring" role="img" aria-label="Healthy skin icon"></div><p class="benefit-icon__label">Healthy Skin</p></div>
      <div class="benefit-icon"><div class="benefit-icon__ring" role="img" aria-label="Natural ingredients icon"></div><p class="benefit-icon__label">Natural<br>Ingredients</p></div>
      <div class="benefit-icon"><div class="benefit-icon__ring" role="img" aria-label="Anti-aging icon"></div><p class="benefit-icon__label">Anti-Aging</p></div>
      <div class="benefit-icon"><div class="benefit-icon__ring" role="img" aria-label="Pores control icon"></div><p class="benefit-icon__label">Pores<br>Control</p></div>
    </div>

    <div class="nutrition">
      <div class="nutrition__header">NUTRITION FACT</div>
      <p class="nutrition__serving">Serving per Container 3</p>
      <div class="nutrition__summary"><span>Serving Sizes</span><strong>250g</strong><span>Calories</span><strong>250g</strong></div>
      <p class="nutrition__amount">Amount Per Saving</p>
      <table class="nutrition__table">
        <tr><td>Total Fat</td><td>15g</td><td>5%</td></tr>
        <tr><td>Trans Fat</td><td>16g</td><td>20%</td></tr>
        <tr><td>Sodium</td><td>17g</td><td>15%</td></tr>
        <tr><td>Sugar</td><td>18g</td><td>18%</td></tr>
        <tr><td>Salt</td><td>12g</td><td>2%</td></tr>
        <tr><td>Protein</td><td>13g</td><td>1%</td></tr>
        <tr><td>Cholesterol</td><td>14g</td><td>8%</td></tr>
        <tr><td>Vitamin A</td><td>7g</td><td>12%</td></tr>
        <tr><td>Vitamin B12</td><td>18g</td><td>20%</td></tr>
      </table>
      <p class="nutrition__note">*Percent daily values are based on a 2,000 calorie diet.</p>
    </div>

    <div class="warning">
      <h3 class="warning__title">WARNING</h3>
      <p class="warning__text">Lorem ipsum dolor sit amet, consectetur adipiscing elit, sed do eiusmod tempor incididunt ut facilisis.</p>
    </div>
    <p class="shelf-life"><span class="shelf-life__title">Manufactured Date</span><br>Best Before 6 Months From<br>Manufactured Date</p>
  </article>
</section>

<section class="label-frame label-frame--drops">
  <article class="label">
    <svg class="label__base" width="1160" height="556" viewBox="0 0 1160 556">
      <defs>
        <linearGradient id="limeBandDrops" x1="0" y1="0" x2="1" y2="0">
          <stop offset="0" stop-color="#c4e033"/>
          <stop offset="0.5" stop-color="#e2fb22"/>
          <stop offset="1" stop-color="#a9c93a"/>
        </linearGradient>
      </defs>
      <rect x="0" y="0" width="1160" height="556" fill="url(#limeBandDrops)"/>
      <polygon points="0,0 1160,0 1160,494 560,494 532,464 0,464" fill="#0c0c0c"/>
    </svg>
    <div class="label__texture" role="img" aria-label="Dark geometric chevron pattern background"></div>
    <svg class="label__base" width="1160" height="556" viewBox="0 0 1160 556" aria-hidden="true">
      <defs>
        <linearGradient id="metalBandDrops" x1="0" y1="0" x2="1" y2="0">
          <stop offset="0" stop-color="#3a3a3a"/>
          <stop offset="0.6" stop-color="#8a8a8a"/>
          <stop offset="1" stop-color="#c8c8c8"/>
        </linearGradient>
      </defs>
      <polyline points="0,462 530,462 558,490 1160,490" fill="none" stroke="#555" stroke-width="4"/>
      <polygon points="0,0 1160,0 1160,32 690,32 660,6 0,6" fill="url(#metalBandDrops)"/>
    </svg>

    <div class="info-block info-block--ingredients">
      <h3 class="info-block__title">INGRIDIENTS</h3>
      <p class="info-block__text">Lorem ipsum dolor sit amet, consectetur adipiscing elit, sed do eiusmod tempor incididunt ut labore et dolore magna aliqua. Quis ipsum suspendisse ultrices gravida. Risus commodo viverra maecenas accumsan lacus vel facilisis.</p>
    </div>
    <div class="info-block info-block--usage">
      <h3 class="info-block__title">HOW TO USE</h3>
      <p class="info-block__text">Lorem ipsum dolor sit amet, consectetur adipiscing elit, sed do eiusmod tempor incididunt ut labore et dolore magna aliqua. Quis ipsum suspendisse ultrices gravida. Risus commodo viverra maecenas accumsan lacus vel facilisis.</p>
    </div>

    <div class="brand">Calm Bloom Wellness</div>
    <h1 class="product-title">
      <span class="product-title__line product-title__line--top">SKIN CARE</span>
      <span class="product-title__line product-title__line--bottom">DROPS</span>
    </h1>
    <div class="count-badge"><span class="count-badge__number">30</span><span class="count-badge__unit">DROPS</span></div>
    <p class="benefits">Beauty &amp; Wellness<br>Improves Comlextions<br>Anti Aging</p>

    <div class="dose"><span class="dose__number">1</span><span class="dose__text">Drop<br>Per Day</span></div>
    <p class="formula-note">Advanced Skin Care Formula</p>

    <div class="benefit-icons">
      <div class="benefit-icon"><div class="benefit-icon__ring" role="img" aria-label="Healthy skin icon"></div><p class="benefit-icon__label">Healthy Skin</p></div>
      <div class="benefit-icon"><div class="benefit-icon__ring" role="img" aria-label="Natural ingredients icon"></div><p class="benefit-icon__label">Natural<br>Ingredients</p></div>
      <div class="benefit-icon"><div class="benefit-icon__ring" role="img" aria-label="Anti-aging icon"></div><p class="benefit-icon__label">Anti-Aging</p></div>
      <div class="benefit-icon"><div class="benefit-icon__ring" role="img" aria-label="Pores control icon"></div><p class="benefit-icon__label">Pores<br>Control</p></div>
    </div>

    <div class="nutrition">
      <div class="nutrition__header">NUTRITION FACT</div>
      <p class="nutrition__serving">Serving per Container 3</p>
      <div class="nutrition__summary"><span>Serving Sizes</span><strong>250g</strong><span>Calories</span><strong>250g</strong></div>
      <p class="nutrition__amount">Amount Per Saving</p>
      <table class="nutrition__table">
        <tr><td>Total Fat</td><td>15g</td><td>5%</td></tr>
        <tr><td>Trans Fat</td><td>16g</td><td>20%</td></tr>
        <tr><td>Sodium</td><td>17g</td><td>15%</td></tr>
        <tr><td>Sugar</td><td>18g</td><td>18%</td></tr>
        <tr><td>Salt</td><td>12g</td><td>2%</td></tr>
        <tr><td>Protein</td><td>13g</td><td>1%</td></tr>
        <tr><td>Cholesterol</td><td>14g</td><td>8%</td></tr>
        <tr><td>Vitamin A</td><td>7g</td><td>12%</td></tr>
        <tr><td>Vitamin B12</td><td>18g</td><td>20%</td></tr>
      </table>
      <p class="nutrition__note">*Percent daily values are based on a 2,000 calorie diet.</p>
    </div>

    <div class="warning">
      <h3 class="warning__title">WARNING</h3>
      <p class="warning__text">Lorem ipsum dolor sit amet, consectetur adipiscing elit, sed do eiusmod tempor incididunt ut facilisis.</p>
    </div>
    <p class="shelf-life"><span class="shelf-life__title">Manufactured Date</span><br>Best Before 6 Months From<br>Manufactured Date</p>
  </article>
</section>

</body>
</html>
```